Business Card Design

I am a new realtor. To stand out from the other 25 realtors in my firm I need a card that will stand out. I am the youngest realtor here, so I want something to reflect that. Something different, as opposed to the same old traditional, boring cards everyone else has. It of course needs to have my picture which I will download for you ( I included a black and white option as well as color. Either are fine) and you can crop it or do whatever you need to make it look the best. Our company colors are red and white. These don't have to be the only colors on the card, but the red especially needs to be a focal color. I like a clean, stream-line look while still eye-catching. Not over the top busy.
While I do have to provide the company logo, I am a contractor. Therefore, I want the focus on me and my information.
Industry/Entity Type
Realtor
Contact Information for Business Card
Marisa Quillon
Realtor (this needs the realtor logo which has the R in the circle at the end)
(office)555.318.4406
(cell) 555.892.6035
Mquillon@brv-homegroup.example
It will also need our company logo which I will download and send
Requirements
Nice to have
- I like the look of the foil or metallic. However, this is definitely not a requirement

```html
<!DOCTYPE html>
<html lang="en">
<head>
<meta charset="utf-8">
<title>Marisa Quillon – Realtor</title>
<link rel="stylesheet" href="https://fonts.googleapis.com/css2?family=Tinos:ital,wght@0,400;0,700;1,400;1,700&display=swap">
<style>
  :root {
    --card-white: #ffffff;
    --brand-red: #d7101f;
    --ink-navy: #1d2240;
    --wave-aqua: #c6eeed;
    --photo-dark: #6b4330;
    --photo-mid: #c9a48c;
    --photo-light: #f1ece8;
  }
  * { margin: 0; padding: 0; box-sizing: border-box; }
  html, body {
    width: 709px; height: 1200px; overflow: hidden;
    background: var(--card-white);
  }
  .card {
    position: relative; width: 709px; height: 1200px; overflow: hidden;
    background: var(--card-white);
    font-family: "Tinos", "Times New Roman", serif;
  }
  .card__art { position: absolute; inset: 0; width: 709px; height: 1200px; }
  .services {
    position: absolute; right: 32px; top: 38px;
    font-style: italic; font-size: 26px; color: var(--ink-navy);
  }
  .specialty {
    position: absolute; right: 32px; top: 112px; text-align: right;
    font-style: italic; font-size: 37px; line-height: 46px; color: var(--brand-red);
  }
  .agent { position: absolute; left: 86px; top: 764px; color: var(--card-white); }
  .agent__name { font-weight: 700; font-size: 66px; line-height: 1; white-space: nowrap; }
  .agent__title { font-style: italic; font-size: 64px; line-height: 1; margin-top: 34px; }
  .contact {
    position: absolute; right: 26px; top: 1072px; text-align: right;
    color: var(--ink-navy); font-size: 31px; line-height: 41px;
  }
  .contact__email { font-style: italic; }
  .contact__label { font-style: italic; }
  .contact__number { font-weight: 700; }
  .brokerage {
    position: absolute; left: 26px; top: 1128px;
    display: flex; align-items: center; gap: 10px;
    color: var(--ink-navy); font-size: 17px; line-height: 21px;
  }
  .brokerage__mark {
    width: 18px; height: 18px; background: var(--brand-red); flex: none;
  }
</style>
</head>
<body>
<div class="card">
  <svg class="card__art" viewBox="0 0 709 1200" xmlns="http://www.w3.org/2000/svg">
    <defs>
      <linearGradient id="portraitTone" x1="0" y1="0" x2="0" y2="1">
        <stop offset="0" stop-color="var(--photo-dark)"/>
        <stop offset="0.35" stop-color="var(--photo-mid)"/>
        <stop offset="0.7" stop-color="var(--photo-light)"/>
        <stop offset="1" stop-color="var(--photo-light)"/>
      </linearGradient>
    </defs>
    <path class="portrait" role="img" aria-label="Portrait photo of the realtor, smiling, in a white blouse and layered bead necklace"
          d="M0,0 L355,0 L355,330 Q500,380 505,480 L505,730 L0,730 Z" fill="url(#portraitTone)"/>
    <rect class="wave-aqua" x="0" y="840" width="709" height="360" fill="var(--wave-aqua)"/>
    <path class="wave-red" fill="var(--brand-red)"
          d="M0,635 C110,745 285,745 430,625 S620,515 709,530 L709,888
             C600,842 470,862 360,932 C250,1002 120,1032 0,992 Z"/>
  </svg>

  <p class="services">Buying • Selling • Renting</p>
  <p class="specialty">Specializing in<br>Longview, Texas</p>

  <div class="agent">
    <h1 class="agent__name">Marisa Quillon</h1>
    <p class="agent__title">Realtor</p>
  </div>

  <div class="brokerage">
    <span class="brokerage__mark"></span>
    <span class="brokerage__name">Harlow Vance<br>Brokerage</span>
  </div>

  <div class="contact">
    <p class="contact__email">Mquillon@brv-homegroup.example</p>
    <p><span class="contact__label">cell</span> <span class="contact__number">555-892-6035</span></p>
    <p><span class="contact__label">office</span> <span class="contact__number">555-318-4406</span></p>
  </div>
</div>
</body>
</html>
```